National Virtual CPA Firm needs post card design

Virtual CPA firm called "QUINDRA" needs a 5.5” x 8.5” post card designed to market our services to middle market mid-size american businesses. We provide Full Service Payroll (includes the processing of payroll, printing of checks and direct depositing, tax filing, and tax payments), Bookkeeping (Using their native systems, or ours), Contract CFO (with expense reduction analysis), Reporting services for business directors to make informed decisions, Capital Fundraising (Advice on seeking equity to help grow your business), and Taxes (Personal (1040), Partnership (1065), Corporate (1120, 1120S (Including Consolidated Returns)), Trust (1041) and Non-Profit (990)), including all affiliated state returns. One of our major selling points is our variety of experience, and our fast turn around times on projects.
This project specifically, I would like to highlight the bookkeeping services, but still want the tax and payroll services listed on the postcard.
I have uploaded the logo design for QUINDRA and would like a postcard that compliments the logo.
Company contact info is:
Quindra accounting services Inc
P.O. Box 4586
Great falls, MT 59471
(800) 362-9174
Www.quindra-example.com
Target Market(s)
Small to medium size businesses
Industry/Entity Type
Accounting

```html
<!DOCTYPE html>
<html lang="en">
<head>
<meta charset="utf-8">
<title>Quindra Postcard</title>
<link href="https://fonts.googleapis.com/css2?family=Open+Sans:wght@400;600;700;800&family=Oswald:wght@500&display=swap" rel="stylesheet">
<style>
  :root{
    --green:#3fae2a;
    --green-dark:#1f8a2e;
    --green-light:#8cc63f;
    --yellow:#fcc419;
    --ink:#231f20;
    --text:#333;
    --bg:#e9e9e9;
    --white:#fff;
  }
  *{box-sizing:border-box;margin:0;padding:0}
  html,body{width:1200px;height:900px;overflow:hidden;background:var(--bg);font-family:"Open Sans",Arial,sans-serif;color:var(--text)}
  .postcard{position:absolute;left:270px;width:660px;height:427px;background:var(--white);overflow:hidden;box-shadow:0 4px 14px rgba(0,0,0,.18)}
  .postcard--front{top:13px}
  .postcard--back{top:460px}
  .card-art{position:absolute;inset:0;width:660px;height:427px}
  .abs{position:absolute}
  .brand{display:flex;align-items:center;gap:10px;font-weight:800;color:var(--ink);letter-spacing:1px;white-space:nowrap}
  .brand__dot{border-radius:50%;background:var(--yellow)}
  .headline{font-weight:800;color:var(--ink);font-size:21px;line-height:1.15;text-transform:uppercase}
  .service{display:flex;gap:10px;align-items:flex-start}
  .service__icon{flex:none;width:30px;height:30px;border-radius:50%;background:var(--green-light);border:2px solid var(--white);box-shadow:0 0 0 1px var(--green-light);display:flex;align-items:center;justify-content:center}
  .service__title{font-weight:800;color:var(--green);font-size:14px;line-height:1.1}
  .service__desc{font-size:10.5px;line-height:1.25;color:var(--text)}
  .pill{background:var(--green-light);color:var(--white);font-weight:800;text-transform:uppercase;border-radius:0 16px 16px 0;padding:5px 20px 5px 16px;font-size:13px;white-space:nowrap}
  .perks{display:flex;justify-content:space-around;width:400px}
  .perk{display:flex;flex-direction:column;align-items:center;gap:4px;color:var(--white);font-weight:800;font-size:11px;text-transform:uppercase}
  .badge{font-family:"Oswald",sans-serif;font-weight:500;color:var(--ink);text-align:center;font-size:14px;line-height:1.05;text-transform:uppercase;width:96px}
  .cta{color:var(--white);width:180px}
  .cta__title{color:var(--yellow);font-weight:800;font-size:14px;line-height:1.2;text-transform:uppercase}
  .cta__line{font-size:14px;font-weight:600;display:flex;align-items:center;gap:6px;margin-top:4px;white-space:nowrap;line-height:1.2}
  .cta__line--web{font-size:12px}
  .cta__dot{width:7px;height:7px;border-radius:50%;background:var(--yellow);display:inline-block}
  .list{display:flex;flex-direction:column;gap:4px;width:340px}
  .list .service__icon{width:22px;height:22px;background:none;border:none;box-shadow:none}
  .list__title{font-weight:800;color:var(--ink);font-size:11.5px;line-height:1.2}
  .list__desc{font-size:10px;line-height:1.2}
  .contact-band{color:var(--white);font-weight:800;font-size:10.5px;line-height:1.3;text-transform:uppercase;width:420px}
  .contact-band em{font-style:normal;color:var(--yellow)}
  .address{font-size:12px;line-height:1.35;color:var(--ink)}
  .indicia{border:1px solid var(--ink);font-size:7.5px;text-align:center;padding:4px 6px;color:var(--ink);white-space:nowrap}
  .indicia span{display:block;line-height:10px}
  .indicia b{font-weight:800}
</style>
</head>
<body>

<section class="postcard postcard--front">
  <svg class="card-art" viewBox="0 0 660 427">
    <defs>
      <linearGradient id="photoWarm" x1="0" y1="0" x2="1" y2="1">
        <stop offset="0" stop-color="#d9a05a"/>
        <stop offset=".45" stop-color="#c9c3bc"/>
        <stop offset="1" stop-color="#6f7f93"/>
      </linearGradient>
      <linearGradient id="bandGreen" x1="0" y1="0" x2="0" y2="1">
        <stop offset="0" stop-color="#3fae2a"/>
        <stop offset="1" stop-color="#1f8a2e"/>
      </linearGradient>
    </defs>
    <path role="img" aria-label="Photo of a person using a tablet surrounded by digital business icons" d="M360 0 H660 V318 H462 C440 220 400 90 360 0Z" fill="url(#photoWarm)"/>
    <path d="M352 0 C392 90 432 220 454 318" fill="none" stroke="var(--green)" stroke-width="14"/>
    <path d="M0 342 Q220 318 448 300 L438 427 H0Z" fill="url(#bandGreen)"/>
    <path d="M462 318 H660 V427 H448 C456 390 462 350 462 318Z" fill="var(--ink)"/>
    <path d="M462 318 C462 350 456 390 448 427" fill="none" stroke="var(--green)" stroke-width="8"/>
    <circle cx="440" cy="300" r="50" fill="var(--yellow)" stroke="var(--white)" stroke-width="4"/>
  </svg>

  <div class="abs brand" style="left:40px;top:26px;font-size:40px">
    <span class="brand__dot" style="width:30px;height:30px"></span>QUINDRA
  </div>

  <h1 class="abs headline" style="left:40px;top:92px">Virtual and remote CPA<br>and accounting services</h1>

  <div class="abs" style="left:40px;top:152px;display:flex;flex-direction:column;gap:10px;width:330px">
    <div class="service">
      <span class="service__icon"><svg width="14" height="14" viewBox="0 0 14 14"><rect x="2" y="1" width="10" height="12" fill="none" stroke="#fff" stroke-width="1.5"/><path d="M4 5h6M4 8h6M4 11h4" stroke="#fff" stroke-width="1.2"/></svg></span>
      <div><div class="service__title">BOOKKEEPING</div><div class="service__desc">Using their native systems, or ours</div></div>
    </div>
    <div class="service">
      <span class="service__icon"><svg width="14" height="14" viewBox="0 0 14 14"><rect x="2" y="1" width="10" height="12" fill="none" stroke="#fff" stroke-width="1.5"/><path d="M5 10l4-6" stroke="#fff" stroke-width="1.2"/><circle cx="5" cy="5" r="1" fill="#fff"/><circle cx="9" cy="9" r="1" fill="#fff"/></svg></span>
      <div><div class="service__title">TAXES</div><div class="service__desc">(Personal (1040), Partnership (1065)</div></div>
    </div>
    <div class="service">
      <span class="service__icon"><svg width="14" height="14" viewBox="0 0 14 14"><rect x="1" y="3" width="12" height="8" fill="none" stroke="#fff" stroke-width="1.5"/><circle cx="7" cy="7" r="2" fill="none" stroke="#fff" stroke-width="1.2"/></svg></span>
      <div><div class="service__title">FULL SERVICE PAYROLL</div><div class="service__desc">includes the processing of payroll, printing of checks and direct depositing, tax filing, and tax payments</div></div>
    </div>
  </div>

  <div class="abs pill" style="left:0;top:304px">Why choose us?</div>

  <div class="abs perks" style="left:10px;top:350px">
    <div class="perk"><svg width="22" height="22" viewBox="0 0 22 22"><circle cx="11" cy="8" r="5" fill="none" stroke="var(--yellow)" stroke-width="2"/><path d="M3 21c1-5 15-5 16 0" fill="none" stroke="var(--yellow)" stroke-width="2"/></svg>Expirienced</div>
    <div class="perk"><svg width="22" height="22" viewBox="0 0 22 22"><circle cx="6" cy="7" r="3" fill="none" stroke="var(--yellow)" stroke-width="2"/><circle cx="16" cy="7" r="3" fill="none" stroke="var(--yellow)" stroke-width="2"/><path d="M1 19c1-5 19-5 20 0" fill="none" stroke="var(--yellow)" stroke-width="2"/></svg>Professional</div>
    <div class="perk"><svg width="22" height="22" viewBox="0 0 22 22"><circle cx="11" cy="9" r="7" fill="none" stroke="var(--yellow)" stroke-width="2"/><path d="M11 5v8M9 7h4M9 11h4" stroke="var(--yellow)" stroke-width="1.5"/></svg>Affordable</div>
  </div>

  <div class="abs badge" style="left:392px;top:278px">Business advisors and consultants</div>

  <div class="abs cta" style="left:474px;top:332px">
    <div class="cta__title">Shedule a free consult now</div>
    <div class="cta__line"><svg width="11" height="11" viewBox="0 0 12 12"><path d="M3 1l2 3-1 1c1 2 2 3 4 4l1-1 3 2-1 2C6 12 0 6 1 2z" fill="var(--yellow)"/></svg>(800) 362-9174</div>
    <div class="cta__line cta__line--web"><span class="cta__dot"></span>QUINDRA-EXAMPLE.COM</div>
  </div>
</section>

<section class="postcard postcard--back">
  <svg class="card-art" viewBox="0 0 660 427">
    <defs>
      <linearGradient id="photoCool" x1="0" y1="0" x2="1" y2="1">
        <stop offset="0" stop-color="#9fb4c6"/>
        <stop offset=".5" stop-color="#4f6f8f"/>
        <stop offset="1" stop-color="#b9c4cc"/>
      </linearGradient>
      <linearGradient id="bandGreen2" x1="0" y1="0" x2="0" y2="1">
        <stop offset="0" stop-color="#3fae2a"/>
        <stop offset="1" stop-color="#1f8a2e"/>
      </linearGradient>
    </defs>
    <path role="img" aria-label="Collage of business meeting and handshake photos in hexagon frames" d="M0 0 H352 C370 60 388 130 400 180 L0 222Z" fill="url(#photoCool)"/>
    <path d="M352 0 C392 100 440 240 462 427" fill="none" stroke="var(--green)" stroke-width="14"/>
    <path d="M0 380 Q220 370 452 356 L456 427 H0Z" fill="url(#bandGreen2)"/>
    <path d="M472 330 H660 V427 H468 C470 395 472 360 472 330Z" fill="var(--ink)"/>
    <path d="M472 330 C472 360 470 395 468 427" fill="none" stroke="var(--green)" stroke-width="8"/>
    <circle cx="440" cy="190" r="50" fill="var(--yellow)" stroke="var(--white)" stroke-width="4"/>
  </svg>

  <div class="abs pill" style="left:0;top:196px;font-size:14px">Our other services</div>

  <div class="abs list" style="left:22px;top:230px">
    <div class="service"><span class="service__icon"><svg width="18" height="18" viewBox="0 0 18 18"><rect x="3" y="2" width="12" height="14" fill="none" stroke="var(--green)" stroke-width="1.5"/><path d="M6 6h6M6 9h6M6 12h4" stroke="var(--green)"/></svg></span><div><div class="list__title">Contract CFO</div><div class="list__desc">with expense reduction analysis</div></div></div>
    <div class="service"><span class="service__icon"><svg width="18" height="18" viewBox="0 0 18 18"><rect x="3" y="2" width="12" height="14" fill="none" stroke="var(--green)" stroke-width="1.5"/><path d="M6 13V9M9 13V6M12 13V10" stroke="var(--green)" stroke-width="1.5"/></svg></span><div><div class="list__title">Reporting Services</div><div class="list__desc">for business directors to make informed decisions</div></div></div>
    <div class="service"><span class="service__icon"><svg width="18" height="18" viewBox="0 0 18 18"><circle cx="9" cy="6" r="3" fill="none" stroke="var(--green)" stroke-width="1.5"/><path d="M3 17c1-5 11-5 12 0" fill="none" stroke="var(--green)" stroke-width="1.5"/></svg></span><div><div class="list__title">Capital Fundraising</div><div class="list__desc">Advice on seeking equity to help grow your business</div></div></div>
    <div class="service"><span class="service__icon"><svg width="18" height="18" viewBox="0 0 18 18"><rect x="3" y="2" width="12" height="14" fill="none" stroke="var(--green)" stroke-width="1.5"/><path d="M6 12l6-6" stroke="var(--green)"/><circle cx="6.5" cy="6.5" r="1" fill="var(--green)"/><circle cx="11.5" cy="11.5" r="1" fill="var(--green)"/></svg></span><div><div class="list__title">Taxes</div><div class="list__desc">(Personal (1040), Partnership (1065), Corporate (1120, 1120S (Including Consolidated Returns))Trust (1041) and Non-Profit (990)), including all affiliated state returns.</div></div></div>
  </div>

  <div class="abs contact-band" style="left:24px;top:388px">Contact <em>QUINDRA</em> to discuss your accounting and CPA needs, and see just how well virtual services may serve you.</div>

  <div class="abs badge" style="left:392px;top:168px">Business advisors and consultants</div>

  <div class="abs indicia" style="left:588px;top:14px">
    <span>PRSRT STD</span><span>ECRWSS</span><span>U.S. Postage</span><span><b>PAID</b></span><span>EDDM RETAIL</span>
  </div>

  <div class="abs brand" style="left:466px;top:80px;font-size:24px">
    <span class="brand__dot" style="width:18px;height:18px"></span>QUINDRA
  </div>
  <div class="abs address" style="left:478px;top:118px">P.O. Box 4586<br>Great falls, MT 59471</div>

  <div class="abs cta" style="left:484px;top:344px">
    <div class="cta__title">Shedule a free consult now</div>
    <div class="cta__line"><svg width="11" height="11" viewBox="0 0 12 12"><path d="M3 1l2 3-1 1c1 2 2 3 4 4l1-1 3 2-1 2C6 12 0 6 1 2z" fill="var(--yellow)"/></svg>(800) 362-9174</div>
    <div class="cta__line cta__line--web"><span class="cta__dot"></span>QUINDRA-EXAMPLE.COM</div>
  </div>
</section>

</body>
</html>
```